Gadgetpickerhelp.com needs your creativity!

We need a website design for a new internet company based in Winnipeg MB called gadgetpickerhelp.com. We provide customers who are relatively new to technology a professional intermediary in the computer buying process. We act as an independent purchasing assistant for our customers by getting a clear understanding of their needs and requirements of their machine and proceed to find a computer with the exact specifications they require at the lowest possible price. Because we are completely independent we do not push any particular brand, OS, or software. We want the website to be bold but streamlined, it should be easy to use and navigate even for a beginner.

Target Market(s)

45+ age bracket

Industry/Entity Type

Internet

Requirements
Must have
• The site must have an About Us page, as well as a secure shopping cart where customers can purchase the service via paylinko and credit card. In this section we will require all of the customer's information to be entered as well as what their needs are for their new computer
I would like a product comparison chart that is broken down into three columns where the features of each service can be checked or unchecked depending on each package. I also need an extended service page, where customers will be able to contact me or directly purchase a remote servicing package
Nice to have
• I would like to have an introductory video for the service provided available to customers on the home page so one click and they will be able to see what our service is about.
Should not have
• Do not use any loud audio or sound clips in the design, subtle sound is fine.

```html
<!DOCTYPE html>
<html lang="en">
<head>
<meta charset="utf-8">
<title>Gadgetpickerhelp.com</title>
<link href="https://fonts.googleapis.com/css2?family=Oswald:wght@500&family=Arimo:wght@400;700&family=Lobster&family=Open+Sans:wght@400&family=Roboto:wght@300;400&display=swap" rel="stylesheet">
<style>
:root{
  --navy:#2b3a42;
  --navy-dark:#1f2b31;
  --page:#eeeeee;
  --card:#ffffff;
  --text:#333a3e;
  --muted:#5b6268;
  --blue1:#3fc0dc;--blue2:#1f8aa6;
  --green1:#9bd13a;--green2:#5c9b16;
  --olive1:#e1d434;--olive2:#a59a12;
  --footer:#8e929c;
  --footer-low:#b3b5bc;
  --link:#0a4d9e;
}
*{box-sizing:border-box;margin:0;padding:0}
html,body{width:1097px;height:1200px;overflow:hidden;background:var(--page)}
.page{position:relative;width:1280px;height:1400px;transform:scale(0.85703);transform-origin:0 0;font-family:"Arimo",sans-serif;color:var(--text);background:var(--page)}
.abs{position:absolute}

.topbar{left:0;top:0;width:1280px;height:69px;background:var(--navy);border-bottom:3px solid #c9ccce}
.nav{left:148px;top:24px;display:flex;gap:32px;font-family:"Oswald",sans-serif;font-size:21px;letter-spacing:.5px;color:#d5dadd}
.nav .active{color:#fff}
.login{left:760px;top:26px;display:flex;gap:8px}
.login .field{width:102px;height:21px;background:#fff;border:1px solid #aaa;font-size:12px;color:#999;padding:3px 0 0 13px}
.login .btn{width:68px;height:21px;background:linear-gradient(#7fc22a,#3f7f0b);color:#fff;font-size:12px;text-align:center;padding-top:3px;border-radius:2px}
.login-links{left:1056px;top:25px;font-size:10px;line-height:13px;color:#fff;letter-spacing:.5px}

.brand{left:150px;top:92px;font-family:"Arimo",sans-serif;font-weight:700;font-size:30px;letter-spacing:1px;color:#2c2f31;display:flex;align-items:center;gap:10px}
.brand .mark{width:14px;height:14px;background:#7ebd2b}
.support{right:149px;top:97px;font-family:"Roboto",sans-serif;font-size:14px;color:#3a3f42}

.slider{left:128px;top:153px;width:1023px;height:385px;background:var(--navy);border-radius:8px;box-shadow:0 3px 6px rgba(0,0,0,.25)}
.hero{left:160px;top:181px;width:962px;height:331px;background:radial-gradient(circle at 30% 25%,#d7ec62 0,#9cc92c 35%,#6c9d10 75%,#4f7c06 100%)}
.hero-visual{left:470px;top:35px;width:390px;height:275px;border-radius:14px;background:linear-gradient(135deg,#3b3f40,#121415);opacity:.85}
.hero h1{left:51px;top:79px;font-family:"Roboto",sans-serif;font-weight:300;font-size:29px;line-height:37px;color:#fff}
.hero p{left:51px;top:161px;width:300px;font-size:12px;line-height:14px;color:#fff}
.watch{left:51px;top:210px;width:188px;height:47px;background:linear-gradient(#2a2a2a,#050505);border-radius:4px;color:#fff;font-family:"Roboto",sans-serif;font-size:19px;padding:12px 0 0 24px;box-shadow:0 2px 3px rgba(0,0,0,.4)}
.watch svg{position:absolute;right:16px;top:14px}
.arrow{top:320px;width:52px;height:53px;border-radius:50%;background:var(--navy)}
.arrow svg{position:absolute;top:17px}

.card{top:573px;width:320px;height:350px;background:var(--card);border-radius:6px;box-shadow:0 0 3px rgba(0,0,0,.2);overflow:visible}
.card-head{left:0;top:0;width:320px;height:74px;background:linear-gradient(#3a4245,#121617);border-radius:6px 6px 0 0}
.card-title{left:0;top:14px;width:320px;text-align:center;font-family:"Lobster",cursive;font-size:23px;color:#fff}
.ribbon{left:40px;top:54px;width:240px;height:40px;clip-path:polygon(0 0,100% 0,94% 50%,100% 100%,0 100%,6% 50%);text-align:center;color:#fff;font-family:"Open Sans",sans-serif;font-size:25px;line-height:40px}
.ribbon small{font-size:21px}
.features{left:30px;top:108px;width:260px;list-style:none}
.features li{height:30px;border-bottom:1px solid #e4e4e4;font-size:12px;letter-spacing:.3px;color:#3b3f42;padding:8px 0 0 47px;position:relative}
.features li svg{position:absolute;left:10px;top:5px}
.buy{left:30px;top:278px;width:260px;height:40px;border-radius:6px;color:#fff;font-family:"Lobster",cursive;font-size:23px;text-align:center;line-height:38px;box-shadow:0 1px 2px rgba(0,0,0,.3)}
.buy svg{display:inline-block;margin-left:16px;vertical-align:-2px}
.blue .ribbon,.blue .buy{background:linear-gradient(var(--blue1),var(--blue2))}
.green .ribbon,.green .buy{background:linear-gradient(var(--green1),var(--green2))}
.olive .ribbon,.olive .buy{background:linear-gradient(var(--olive1),var(--olive2))}

.band{left:0;top:963px;width:1280px;height:33px;background:var(--navy);border-top:2px solid #46555d}
.footer{left:0;top:996px;width:1280px;height:338px;background:var(--footer)}
.footer-low{left:0;top:1334px;width:1280px;height:66px;background:var(--footer-low);border-top:2px dashed #c6c8cd}
.divider{top:1040px;height:272px;border-left:2px dashed #a9adb5}
.col-title{font-family:"Lobster",cursive;font-size:24px;color:#fff;text-shadow:0 1px 1px rgba(0,0,0,.3)}
.col-icon{width:28px;height:28px;border-radius:50%;background:#d8dbe0}
.ftext{font-size:13px;line-height:20px;color:#fff}
.ftext a{color:var(--link);text-decoration:none}
.ago{font-size:12px;color:#fff}
.email-label{left:510px;top:1156px;font-size:13px;color:#fff}
.email-input{left:510px;top:1179px;width:277px;height:30px;background:#eeeeee;border:1px solid #c8c8c8;border-radius:2px}
.subscribe{left:510px;top:1227px;width:276px;height:38px;background:linear-gradient(var(--green1),var(--green2));border-radius:3px;color:#fff;font-family:"Lobster",cursive;font-size:17px;text-align:center;line-height:36px;box-shadow:0 1px 2px rgba(0,0,0,.3)}
.contact-row{left:855px;display:flex;align-items:center;gap:20px;font-family:"Open Sans",sans-serif;font-size:15px;color:#fff}
.contact-row .disc{width:44px;height:44px;border-radius:50%;background:#a6aab2;display:flex;align-items:center;justify-content:center}
.copyright{left:161px;top:1363px;font-size:12px;color:#555a60}
.follow{left:970px;top:1350px;font-family:"Lobster",cursive;font-size:23px;color:#fff}
.social{top:1355px;width:21px;height:21px;background:#7e828a;border-radius:2px}
</style>
</head>
<body>
<div class="page">

  <header class="abs topbar"></header>
  <nav class="abs nav">
    <span class="active">HOME</span><span>ABOUT</span><span>PACKAGES</span><span>TESTIMONIALS</span><span>FAQ</span><span>CONTACT</span>
  </nav>
  <div class="abs login">
    <div class="field">Username</div><div class="field">Password</div><div class="btn">Login</div>
  </div>
  <div class="abs login-links">Forgot Password?<br>Register</div>

  <div class="abs brand"><span>GADGETPICKERHELP</span><span class="mark"></span></div>
  <div class="abs support">24/7 Sales &amp; Support &nbsp;&nbsp;+1 800 555 0142</div>

  <section class="abs slider"></section>
  <div class="abs arrow" style="left:102px"><svg width="52" height="20" viewBox="0 0 52 20"><path d="M27 2 L19 10 L27 18" stroke="#9aa5ab" stroke-width="3" fill="none"/></svg></div>
  <div class="abs arrow" style="left:1125px"><svg width="52" height="20" viewBox="0 0 52 20"><path d="M31 2 L39 10 L31 18" stroke="#9aa5ab" stroke-width="3" fill="none"/></svg></div>
  <div class="abs hero">
    <div class="abs hero-visual" role="img" aria-label="Product photo of two black computer towers with green drive bays"></div>
    <h1 class="abs">Gadget Picker Help<br>Packages</h1>
    <p class="abs">sit amet, consectetur adipiscing elit. In interdum aliquet orci, vitae ornare erat elementum et.</p>
    <div class="abs watch">WATCH VIDEO<svg width="14" height="20" viewBox="0 0 14 20"><path d="M3 2 L11 10 L3 18" stroke="#fff" stroke-width="3.5" fill="none"/></svg></div>
  </div>

  <article class="abs card blue" style="left:128px">
    <div class="abs card-head"></div>
    <div class="abs card-title">Exceptional Value Package</div>
    <div class="abs ribbon">$ 79 / <small>month</small></div>
    <ul class="abs features">
      <li><svg width="20" height="18" viewBox="0 0 20 18"><path d="M2 9 L8 15 L18 2" stroke="#3f9a1c" stroke-width="4" fill="none"/></svg>Hard Disk 120GB</li>
      <li><svg width="20" height="18" viewBox="0 0 20 18"><path d="M2 9 L8 15 L18 2" stroke="#3f9a1c" stroke-width="4" fill="none"/></svg>VGA 512GHz</li>
      <li><svg width="20" height="18" viewBox="0 0 20 18"><path d="M2 9 L8 15 L18 2" stroke="#3f9a1c" stroke-width="4" fill="none"/></svg>Bluetooth</li>
      <li><svg width="20" height="18" viewBox="0 0 20 18"><path d="M2 9 L8 15 L18 2" stroke="#3f9a1c" stroke-width="4" fill="none"/></svg>Dual Core Vantix Processor</li>
      <li><svg width="20" height="18" viewBox="0 0 20 18"><path d="M2 9 L8 15 L18 2" stroke="#3f9a1c" stroke-width="4" fill="none"/></svg>1 Year Waranty</li>
    </ul>
    <div class="abs buy">Buy Now<svg width="14" height="20" viewBox="0 0 14 20"><path d="M3 2 L11 10 L3 18" stroke="#fff" stroke-width="3.5" fill="none"/></svg></div>
  </article>

  <article class="abs card green" style="left:480px">
    <div class="abs card-head"></div>
    <div class="abs card-title">Extended Service Package</div>
    <div class="abs ribbon">$ 159 / <small>month</small></div>
    <ul class="abs features">
      <li><svg width="20" height="18" viewBox="0 0 20 18"><path d="M2 9 L8 15 L18 2" stroke="#3f9a1c" stroke-width="4" fill="none"/></svg>Hard Disk 120GB</li>
      <li><svg width="20" height="18" viewBox="0 0 20 18"><path d="M2 9 L8 15 L18 2" stroke="#3f9a1c" stroke-width="4" fill="none"/></svg>VGA 512GHz</li>
      <li><svg width="20" height="18" viewBox="0 0 20 18"><path d="M2 9 L8 15 L18 2" stroke="#3f9a1c" stroke-width="4" fill="none"/></svg>Bluetooth</li>
      <li><svg width="20" height="18" viewBox="0 0 20 18"><path d="M2 9 L8 15 L18 2" stroke="#3f9a1c" stroke-width="4" fill="none"/></svg>Dual Core Vantix Processor</li>
      <li><svg width="20" height="18" viewBox="0 0 20 18"><path d="M2 9 L8 15 L18 2" stroke="#3f9a1c" stroke-width="4" fill="none"/></svg>1 Year Waranty</li>
    </ul>
    <div class="abs buy">Buy Now<svg width="14" height="20" viewBox="0 0 14 20"><path d="M3 2 L11 10 L3 18" stroke="#fff" stroke-width="3.5" fill="none"/></svg></div>
  </article>

  <article class="abs card olive" style="left:832px">
    <div class="abs card-head"></div>
    <div class="abs card-title">Full Service Package</div>
    <div class="abs ribbon">$ 95 / <small>month</small></div>
    <ul class="abs features">
      <li><svg width="20" height="18" viewBox="0 0 20 18"><path d="M2 9 L8 15 L18 2" stroke="#3f9a1c" stroke-width="4" fill="none"/></svg>Hard Disk 120GB</li>
      <li><svg width="20" height="18" viewBox="0 0 20 18"><path d="M2 9 L8 15 L18 2" stroke="#3f9a1c" stroke-width="4" fill="none"/></svg>VGA 512GHz</li>
      <li><svg width="20" height="18" viewBox="0 0 20 18"><path d="M2 9 L8 15 L18 2" stroke="#3f9a1c" stroke-width="4" fill="none"/></svg>Bluetooth</li>
      <li><svg width="20" height="18" viewBox="0 0 20 18"><path d="M2 9 L8 15 L18 2" stroke="#3f9a1c" stroke-width="4" fill="none"/></svg>Dual Core Vantix Processor</li>
      <li><svg width="20" height="18" viewBox="0 0 20 18"><path d="M2 9 L8 15 L18 2" stroke="#3f9a1c" stroke-width="4" fill="none"/></svg>1 Year Waranty</li>
    </ul>
    <div class="abs buy">Buy Now<svg width="14" height="20" viewBox="0 0 14 20"><path d="M3 2 L11 10 L3 18" stroke="#fff" stroke-width="3.5" fill="none"/></svg></div>
  </article>

  <div class="abs band"></div>
  <footer class="abs footer"></footer>
  <div class="abs divider" style="left:467px"></div>
  <div class="abs divider" style="left:815px"></div>

  <div class="abs col-icon" style="left:161px;top:1024px"></div>
  <h2 class="abs col-title" style="left:205px;top:1020px">Chatter Updates</h2>
  <div class="abs ftext" style="left:161px;top:1072px;width:270px">Nunc tristique mi ac turpis placerat quis sollicitudin metus condimentum. <a>#Donec sed nunc in lacus fermentum ultrices</a> ut eu turpis. Quisque sodales turpis ut risus dignissim non</div>
  <div class="abs ago" style="left:161px;top:1158px">10 days ago</div>
  <div class="abs ftext" style="left:161px;top:1192px;width:270px">Nunc tristique mi ac turpis placerat quis sollicitudin metus condimentum. <a>#Donec sed nunc in lacus fermentum ultrices</a> ut eu turpis. Quisque sodales turpis ut risus dignissim non</div>
  <div class="abs ago" style="left:161px;top:1278px">10 days ago</div>

  <div class="abs col-icon" style="left:510px;top:1024px"></div>
  <h2 class="abs col-title" style="left:565px;top:1020px">Newsletter Signup</h2>
  <div class="abs ftext" style="left:510px;top:1072px;width:275px">Cras volutpat, ante ac gravida iaculis, dui lacus iaculis nibh, eu scelerisque arcu diam a augue. Donec imperdiet pharetra fringilla.</div>
  <div class="abs email-label">Your Email Address</div>
  <div class="abs email-input"></div>
  <div class="abs subscribe">Subscibe to stay updated with us!</div>

  <div class="abs col-icon" style="left:855px;top:1024px"></div>
  <h2 class="abs col-title" style="left:917px;top:1020px">Contact Us</h2>
  <div class="abs contact-row" style="top:1075px">
    <span class="disc"><svg width="22" height="22" viewBox="0 0 24 24"><path d="M6 3 L10 3 L11 8 L8.5 9.5 C10 13 11 14 14.5 15.5 L16 13 L21 14 L21 18 C21 20 19 21 17 21 C10 20 4 14 3 7 C3 5 4 3 6 3 Z" fill="#555"/></svg></span>
    <span>(012) 555 010 4471</span>
  </div>
  <div class="abs contact-row" style="top:1140px">
    <span class="disc"><svg width="22" height="22" viewBox="0 0 24 24"><rect x="6" y="3" width="12" height="6" fill="#555"/><rect x="3" y="9" width="18" height="8" rx="1" fill="#555"/><rect x="6" y="15" width="12" height="6" fill="#777"/></svg></span>
    <span>(012) 555 018 2290</span>
  </div>
  <div class="abs contact-row" style="top:1207px">
    <span class="disc"><svg width="22" height="22" viewBox="0 0 24 24"><rect x="3" y="6" width="18" height="13" fill="#e8d9a6"/><path d="M3 6 L12 13 L21 6" stroke="#a8975c" stroke-width="1.5" fill="none"/></svg></span>
    <span>info@gadgetpickerhelp.com</span>
  </div>

  <div class="abs footer-low"></div>
  <div class="abs copyright">All Rights Reserved © gadgetpickerhelp.com</div>
  <div class="abs follow">Follow Us</div>
  <div class="abs social" style="left:1080px"></div>
  <div class="abs social" style="left:1110px"></div>

</div>
</body>
</html>
```